Web Page Flash Animation Needed

We are looking for a Flash animation element for our website Home page. Essentially what we are envisioning is using the attached photo of a painting to create a "jigsaw puzzle" which comes together (animation) to display the painting, with each piece of the puzzle being a link to each page of our site. Attached you will also see a sketch of sort of how we envision this looking, along with a list of the individual pages of our website.

We are thinking that the size of the Flash element should be so that it fits on a single screen (no scrolling) of most modern monitors. We're looking for a lot of creativity - so if you have a better way of doing this - even if it's not Flash - we are open to alternative ideas.

*I have included a copy of our logo - I believe what we envision is 8 puzzle pieces: 7 for each of the site pages and the other for our logo. The pieces come in and together as the page loads. Again, open to alternate ideas & creativity.

Please reach out to me with any questions regarding the project.

Industry/Entity Type

Painting

```html
<!DOCTYPE html>
<html lang="en">
<head>
<meta charset="utf-8">
<title>Orrin — Home</title>
<link rel="stylesheet" href="https://fonts.googleapis.com/css2?family=Cinzel:wght@600;700&display=swap">
<style>
  :root {
    --backdrop: #221b15;
    --backdrop-weave: #1b1510;
    --piece-edge: #ffffff;
    --paint-deep: #2f0a0c;
    --paint-mid: #6e1216;
    --paint-bright: #a3191c;
    --label: #ffffff;
  }
  html, body {
    margin: 0;
    width: 1200px;
    height: 835px;
    overflow: hidden;
    background: var(--backdrop);
  }
  .stage {
    width: 1200px;
    height: 835px;
    background:
      repeating-linear-gradient(45deg, var(--backdrop-weave) 0 1px, transparent 1px 4px),
      var(--backdrop);
  }
  .puzzle-board {
    display: block;
    width: 1200px;
    height: 835px;
  }
  .piece-shape {
    fill: url(#painting-tone);
    stroke: var(--piece-edge);
    stroke-width: 3;
    stroke-linejoin: round;
    filter: drop-shadow(0 0 4px rgba(0,0,0,0.8));
  }
  .piece-link:hover .piece-shape {
    fill: url(#painting-tone-lit);
  }
  .piece-label {
    fill: var(--label);
    font-family: "Cinzel", "Times New Roman", serif;
    font-weight: 700;
    font-size: 22px;
    text-anchor: middle;
    dominant-baseline: middle;
    letter-spacing: 0.2px;
  }
  .piece-label--small { font-size: 15px; }
  .piece-label--brand { font-size: 26px; letter-spacing: 2px; }
</style>
</head>
<body>
<main class="stage">
  <svg class="puzzle-board" viewBox="0 0 1100 765" preserveAspectRatio="none" xmlns="http://www.w3.org/2000/svg">
    <defs>
      <linearGradient id="painting-tone" gradientUnits="userSpaceOnUse" x1="340" y1="15" x2="770" y2="745">
        <stop offset="0" stop-color="var(--paint-mid)"/>
        <stop offset="0.3" stop-color="var(--paint-deep)"/>
        <stop offset="0.55" stop-color="var(--paint-mid)"/>
        <stop offset="0.75" stop-color="var(--paint-bright)"/>
        <stop offset="1" stop-color="var(--paint-deep)"/>
      </linearGradient>
      <linearGradient id="painting-tone-lit" gradientUnits="userSpaceOnUse" x1="340" y1="15" x2="770" y2="745">
        <stop offset="0" stop-color="#8a1a1e"/>
        <stop offset="0.5" stop-color="#b0232a"/>
        <stop offset="1" stop-color="#5a1012"/>
      </linearGradient>
    </defs>

    <g class="puzzle-pieces" role="img" aria-label="Red oil painting with broad brushstrokes, cut into eight jigsaw pieces">
      <a class="piece-link" href="#about">
        <path class="piece-shape" d="M385,55 L456,55 C464,63 440,69 442,83 C444,99 496,99 498,83 C500,69 476,63 484,55 L556,55 L556,116 C564,124 570,100 584,102 C600,104 600,156 584,158 C570,160 564,136 556,144 L556,202 L484,202 C476,194 500,188 498,174 C496,158 444,158 442,174 C440,188 464,194 456,202 L385,202 L385,144 C377,136 371,160 357,158 C341,156 341,104 357,102 C371,100 377,124 385,116 Z"/>
        <text class="piece-label" x="466" y="133">ABOUT</text>
      </a>
      <a class="piece-link" href="#home">
        <path class="piece-shape" d="M556,55 L626,55 C634,47 610,41 612,27 C614,11 666,11 668,27 C670,41 646,47 654,55 L723,55 L723,116 C715,124 709,100 695,102 C679,104 679,156 695,158 C709,160 715,136 723,144 L723,202 L654,202 C646,210 670,216 668,230 C666,246 614,246 612,230 C610,216 634,210 626,202 L556,202 L556,144 C564,136 570,160 584,158 C600,156 600,104 584,102 C570,100 564,124 556,116 Z"/>
        <text class="piece-label piece-label--brand" x="638" y="132">ORRIN</text>
      </a>
      <a class="piece-link" href="#team">
        <path class="piece-shape" d="M385,202 L456,202 C464,194 440,188 442,174 C444,158 496,158 498,174 C500,188 476,194 484,202 L556,202 L556,276 C548,284 542,260 528,262 C512,264 512,316 528,318 C542,320 548,296 556,304 L556,377 L484,377 C476,369 500,363 498,349 C496,333 444,333 442,349 C440,363 464,369 456,377 L385,377 L385,304 C393,296 399,320 413,318 C429,316 429,264 413,262 C399,260 393,284 385,276 Z"/>
        <text class="piece-label" x="468" y="293">TEAM</text>
      </a>
      <a class="piece-link" href="#products">
        <path class="piece-shape" d="M556,202 L626,202 C634,210 610,216 612,230 C614,246 666,246 668,230 C670,216 646,210 654,202 L723,202 L723,276 C731,284 737,260 751,262 C767,264 767,316 751,318 C737,320 731,296 723,304 L723,377 L654,377 C646,369 670,363 668,349 C666,333 614,333 612,349 C610,363 634,369 626,377 L556,377 L556,304 C548,296 542,320 528,318 C512,316 512,264 528,262 C542,260 548,284 556,276 Z"/>
        <text class="piece-label" x="636" y="293">PRODUCTS</text>
      </a>
      <a class="piece-link" href="#clients">
        <path class="piece-shape" d="M385,377 L456,377 C464,369 440,363 442,349 C444,333 496,333 498,349 C500,363 476,369 484,377 L556,377 L556,436 C564,444 570,420 584,422 C600,424 600,476 584,478 C570,480 564,456 556,464 L556,524 L484,524 C476,516 500,510 498,496 C496,480 444,480 442,496 C440,510 464,516 456,524 L385,524 L385,464 C377,456 371,480 357,478 C341,476 341,424 357,422 C371,420 377,444 385,436 Z"/>
        <text class="piece-label" x="468" y="447">CLIENTS</text>
      </a>
      <a class="piece-link" href="#news">
        <path class="piece-shape" d="M556,377 L626,377 C634,369 610,363 612,349 C614,333 666,333 668,349 C670,363 646,369 654,377 L723,377 L723,436 C715,444 709,420 695,422 C679,424 679,476 695,478 C709,480 715,456 723,464 L723,524 L654,524 C646,532 670,538 668,552 C666,568 614,568 612,552 C610,538 634,532 626,524 L556,524 L556,464 C564,456 570,480 584,478 C600,476 600,424 584,422 C570,420 564,444 556,436 Z"/>
        <text class="piece-label" x="636" y="447">NEWS</text>
      </a>
      <a class="piece-link" href="#contact">
        <path class="piece-shape" d="M385,524 L456,524 C464,516 440,510 442,496 C444,480 496,480 498,496 C500,510 476,516 484,524 L556,524 L556,596 C548,604 542,580 528,582 C512,584 512,636 528,638 C542,640 548,616 556,624 L556,698 L484,698 C476,706 500,712 498,726 C496,742 444,742 442,726 C440,712 464,706 456,698 L385,698 L385,624 C393,616 399,640 413,638 C429,636 429,584 413,582 C399,580 393,604 385,596 Z"/>
        <text class="piece-label piece-label--small" x="470" y="610">CONTACT</text>
      </a>
      <a class="piece-link" href="#social">
        <path class="piece-shape" d="M556,524 L626,524 C634,532 610,538 612,552 C614,568 666,568 668,552 C670,538 646,532 654,524 L723,524 L723,596 C731,604 737,580 751,582 C767,584 767,636 751,638 C737,640 731,616 723,624 L723,698 L654,698 C646,690 670,684 668,670 C666,654 614,654 612,670 C610,684 634,690 626,698 L556,698 L556,624 C548,616 542,640 528,638 C512,636 512,584 528,582 C542,580 548,604 556,596 Z"/>
        <text class="piece-label" x="636" y="617">SOCIAL</text>
      </a>
    </g>
  </svg>
</main>
</body>
</html>
```